Plakate für TQ Car Wash
Zielgruppe
TQ Car Wash
SB Waschpark mit 4 Plätzen
Zielgruppe: Alle Autofahrer aus der Region
Marketing wg. Neueröffnung
Aufgabenstellung
Design ist für zwei Planen an einem Werbeanhänger
2200mm x 4750mm Fläche
Aussagen, Logo (kann ähnlich sein oder als eps bzw ai geliefert werden) als Ideenskizze in den Dateien mitgeliwfert. Open to new ideas.

```html
<!DOCTYPE html>
<html lang="de">
<head>
<meta charset="utf-8">
<title>TQ Car Wash – Plane Werbeanhänger</title>
<link rel="stylesheet" href="https://fonts.googleapis.com/css2?family=Archivo:ital,wght@0,400;0,800;0,900;1,600;1,900&display=swap">
<style>
  :root {
    --navy: #23466d;
    --sky: #27ade3;
    --red: #e31f26;
    --white: #ffffff;
    --paper: #fdfdfd;
    --frame: #333333;
  }
  * { margin: 0; padding: 0; box-sizing: border-box; }
  html, body { width: 1000px; height: 1200px; overflow: hidden; background: var(--paper); }
  .canvas { position: relative; width: 1000px; height: 1200px; font-family: "Archivo", Arial, sans-serif; }

  .brand-name {
    position: absolute;
    color: var(--navy);
    font-weight: 900;
    letter-spacing: -1px;
    white-space: nowrap;
    line-height: 1;
    text-align: center;
  }
  .brand-name--hero { left: 0; width: 1000px; top: 340px; font-size: 128px; }

  .banner {
    position: absolute;
    left: 33px; top: 693px;
    width: 934px; height: 432px;
    border: 1px solid var(--frame);
    background: var(--white);
    overflow: hidden;
  }
  .banner__visual {
    position: absolute;
    left: 18px; top: 36px;
    width: 520px; height: 250px;
    border-radius: 120px 140px 60px 60px;
    background: radial-gradient(ellipse at 55% 60%, #2c5582 0%, #23466d 35%, #8fd1ef 62%, #e6f6fd 85%);
  }
  .banner .brand-name--small { left: 0; width: 546px; top: 310px; font-size: 66px; }

  .offer {
    position: absolute;
    left: 547px; top: 0;
    width: 387px; height: 100%;
    background: var(--red);
    color: var(--white);
  }
  .offer__bubbles { position: absolute; inset: 0; }
  .offer__slogan {
    position: absolute;
    left: 90px; top: 68px;
    font-weight: 900;
    font-style: italic;
    font-size: 54px;
    line-height: 72px;
  }
  .offer__rule {
    position: absolute;
    left: 37px; top: 317px;
    width: 308px; height: 2px;
    background: var(--white);
  }
  .offer__pin { position: absolute; left: 48px; top: 342px; }
  .offer__address {
    position: absolute;
    left: 106px; top: 340px;
    font-weight: 600;
    font-style: italic;
    font-size: 21px;
    line-height: 28px;
  }
</style>
</head>
<body>
<div class="canvas">
  <div class="brand-name brand-name--hero">TQ Car Wash</div>

  <section class="banner">
    <div class="banner__visual" role="img" aria-label="Illustration: Auto-Silhouette in Dunkelblau umgeben von hellblauen Schaumwolken und Funkeln"></div>
    <div class="brand-name brand-name--small">TQ Car Wash</div>

    <div class="offer">
      <svg class="offer__bubbles" width="387" height="432" viewBox="0 0 387 432" aria-hidden="true">
        <g fill="none" stroke="#ffffff" stroke-width="2">
          <circle cx="250" cy="135" r="6.5"/>
          <circle cx="55" cy="197" r="9"/>
          <circle cx="45" cy="243" r="12"/>
        </g>
      </svg>
      <div class="offer__slogan">Einfach<br>Besser<br>Sauber</div>
      <div class="offer__rule"></div>
      <svg class="offer__pin" width="40" height="55" viewBox="0 0 40 55" aria-hidden="true">
        <path d="M20 52 C 8 36, 2 28, 2 20 A 18 18 0 0 1 38 20 C 38 28, 32 36, 20 52 Z" fill="none" stroke="#ffffff" stroke-width="3.5"/>
        <circle cx="20" cy="20" r="8" fill="#ffffff"/>
      </svg>
      <div class="offer__address">In Birkenfehn<br>hinter der Feuerwehr</div>
    </div>
  </section>
</div>
</body>
</html>
```